Electrical contractor

looking for a standard sized, horizontal, double sided business card for an electrical contractors business.
i have played around on microsoft word (only computer program i know how to use!) and will attach what i have made so far, really open to any ideas. i just want the DORB to stand out to the rest of the business name.

i wish to use the colours black and green, and white for writing. i will attach the pictures i took off google, i want to either use them, or somethin similar for the back grounds

i wish the front to have the following info:
business name: D.O.R.B ELECTRICAL CONTRACTORS
MY NAME; CORBIN HOLT
STATUS; A CLASS ELECTRICIAN
LICENSE NO; TRN517394
PH NO. 0431576204
EMAIL ADD. DORB.ELECTRICAL@VELTOMAIL.COM
AND MY SLOGAN: where excellence meets integrity, and service comes with a smile.

i am not sure what to have on the back, other than what i do for work.eg titled WHAT WE DO
i dont want too much written on there or will look crowded, but options to add to back, from most important to least, please pick however many you think will look the best
new homes/extentions
led lighting and downlights
Solar Power
power
safety switches
switchboards
telephone and tv
smoke alarms
stoves and ovens
hot water systems
fault finding
re wiring
Updates

Thank you to those who have submitted designs, I would like to change my slogan to something more simple, I'm thinking something like. RELIABLE. EFFICIENT. PROFESSIONAL. AFFORDABLE. in what ever order you thinks fits best. Thanks

Industry/Entity Type

Contractor

```html
<!DOCTYPE html>
<html lang="en">
<head>
<meta charset="utf-8">
<title>D.O.R.B Electrical Contractors – Business Card</title>
<link rel="stylesheet" href="https://fonts.googleapis.com/css2?family=Roboto+Condensed:wght@400;700&display=swap">
<style>
  :root {
    --page: #ececec;
    --black: #000000;
    --deep-green: #1c5a0c;
    --mid-green: #4aa518;
    --bright-green: #9ee01a;
    --lime: #c6e62a;
    --lime-text: #d8f02a;
    --glow-core: #e8f21c;
    --white: #ffffff;
    --band-text: #142000;
  }
  * { margin: 0; padding: 0; box-sizing: border-box; }
  html, body {
    width: 1200px;
    height: 973px;
    overflow: hidden;
    background: var(--page);
    font-family: "Roboto Condensed", "Arial Narrow", sans-serif;
  }
  .card {
    position: absolute;
    left: 250px;
    width: 700px;
    height: 400px;
    overflow: hidden;
    background:
      radial-gradient(circle at 24% 68%, var(--bright-green) 0, var(--mid-green) 22%, var(--deep-green) 46%, var(--black) 74%);
    box-shadow: 0 6px 18px rgba(0,0,0,0.18);
  }
  .card--back { top: 60px; }
  .card--front { top: 513px; }

  .illustration-area {
    position: absolute;
    left: 0;
    top: 0;
    width: 340px;
    height: 100%;
    background: radial-gradient(ellipse at 45% 62%, var(--glow-core) 0, rgba(200,230,30,0.55) 28%, rgba(80,160,20,0) 62%);
  }

  .brand {
    position: absolute;
    right: 40px;
    top: 30px;
    color: var(--lime);
    font-weight: 700;
    text-align: right;
    letter-spacing: 3px;
    line-height: 1;
  }
  .brand__name { display: block; font-size: 52px; letter-spacing: 6px; }
  .brand__tag { display: block; font-size: 17px; margin-top: 6px; }

  .services {
    position: absolute;
    right: 40px;
    top: 140px;
    list-style: none;
    text-align: center;
    color: var(--lime-text);
    font-size: 22px;
    line-height: 31px;
  }

  .contact {
    position: absolute;
    left: 370px;
    top: 148px;
    color: var(--white);
    font-size: 17px;
    line-height: 27px;
    text-transform: uppercase;
  }
  .contact__name { font-weight: 700; font-size: 23px; }
  .contact__role { padding-left: 26px; margin-bottom: 12px; }
  .contact__line { display: flex; align-items: center; gap: 8px; }
  .contact__icon { width: 17px; height: 17px; flex: none; }

  .slogan-band {
    position: absolute;
    left: 0;
    right: 0;
    bottom: 0;
    height: 44px;
    background: var(--lime);
    color: var(--band-text);
    font-size: 22px;
    line-height: 44px;
    text-align: right;
    padding-right: 40px;
  }
</style>
</head>
<body>

<section class="card card--back" aria-label="Card back: services">
  <div class="illustration-area" role="img" aria-label="Illustration of a glowing yellow-green light bulb"></div>
  <div class="brand"><span class="brand__name">D.O.R.B</span><span class="brand__tag">ELECTRICAL CONTRACTORS</span></div>
  <ul class="services">
    <li>New Homes/extentions</li>
    <li>LED Lighting and Downlights</li>
    <li>Solar Power | Safety Switches</li>
    <li>Switchboards | Telephone and TV</li>
    <li>Smoke Alarms | Stoves and Ovens</li>
    <li>Hot Water Systems | Re Wiring</li>
    <li>Fault Finding</li>
  </ul>
</section>

<section class="card card--front" aria-label="Card front: contact details">
  <div class="illustration-area" role="img" aria-label="Illustration of a glowing yellow-green light bulb"></div>
  <div class="brand"><span class="brand__name">D.O.R.B</span><span class="brand__tag">ELECTRICAL CONTRACTORS</span></div>
  <div class="contact">
    <p class="contact__name">Corbin Holt</p>
    <p class="contact__role">A Class Electrician</p>
    <p>License No; TRN517394</p>
    <p class="contact__line">
      <svg class="contact__icon" viewBox="0 0 18 18" aria-hidden="true"><circle cx="9" cy="9" r="9" fill="#fff"/><path d="M6 4.5l2 2-1 1.2c.6 1.3 1.6 2.3 2.9 2.9l1.2-1 2 2-1.3 1.6C8.8 13 5 9.2 4.8 5.8z" fill="#000"/></svg>
      0431576204
    </p>
    <p class="contact__line">
      <svg class="contact__icon" viewBox="0 0 18 18" aria-hidden="true"><circle cx="9" cy="9" r="9" fill="#fff"/><rect x="4" y="5.5" width="10" height="7" fill="none" stroke="#000" stroke-width="1.3"/><path d="M4 5.5l5 4 5-4" fill="none" stroke="#000" stroke-width="1.3"/></svg>
      DORB.ELECTRICAL@VELTOMAIL.COM
    </p>
  </div>
  <p class="slogan-band">Where excellence meets integrity, and service comes with a smile.</p>
</section>

</body>
</html>
```